50% off blue price stickers - poster

I am looking for a poster to hang in our retail discount store that let's people know they take 50% off the marked price on anything with a blue price sticker. We try and tell them as they walk in but can't catch everyone. If they don't know, they don't see the value in the pricing. We mark the retail price with a blue price tag and they get 50% off that price. We sell items from wholesale clubs (Valmo, JEDs Depot) and offer 50% off what they sell the items for. Clothes, Housewares, Kitchenware, Furniture, Bath and Body, Electronics, Jewelry - you name it.
Updates

Check out our Linkpage page - Marla's Double Delight, in Brentwood, California to learn more about us and our merchandise.

For poster size - we are looking at 20" wide by 30" long. Thank you.

Target Market(s)

Ages 35-50

Industry/Entity Type

Retail

Font styles to use
Serif

Requirements
Must have
• Store name - Marla's Double Delight
Nice to have
• Not too cluttered - easy to read to get the point across quickly. Something that incorporates our logo - but doesn't have to stick with the red/black theme, especially if you are using blue themes in the poster. Maybe just use the theme of the logo so the fonts are similar....

```html
<!DOCTYPE html>
<html lang="en">
<head>
<meta charset="utf-8">
<title>50% Off – Marla's Double Delight</title>
<link rel="stylesheet" href="https://fonts.googleapis.com/css2?family=Open+Sans:ital,wght@0,700;0,800;1,800&display=swap">
<style>
  :root {
    --frame-navy: #1b4a82;
    --poster-blue: #1f73c4;
    --shadow-blue: #1961ab;
    --light-blue: #3d8fd8;
    --paper: #ffffff;
    --brand-blue: #1f73c4;
  }
  * { margin: 0; padding: 0; box-sizing: border-box; }
  html, body {
    width: 839px;
    height: 1200px;
    overflow: hidden;
    background: var(--paper);
  }
  .poster {
    position: relative;
    width: 839px;
    height: 1200px;
    background: var(--frame-navy);
    padding: 22px;
    font-family: "Open Sans", Arial, sans-serif;
  }
  .sale-panel {
    position: relative;
    width: 100%;
    height: 1012px;
    background: var(--poster-blue);
    overflow: hidden;
  }
  .long-shadows {
    position: absolute;
    inset: 0;
    width: 100%;
    height: 100%;
  }
  .headline-percent,
  .headline-off,
  .sticker-note,
  .category-list {
    position: absolute;
    left: 0;
    width: 100%;
    color: var(--paper);
    text-align: center;
  }
  .headline-percent {
    top: 20px;
    font-weight: 800;
    font-size: 340px;
    line-height: 1;
    letter-spacing: -0.05em;
  }
  .headline-off {
    top: 372px;
    font-weight: 800;
    font-style: italic;
    font-size: 370px;
    line-height: 1;
    letter-spacing: -0.04em;
  }
  .sticker-note {
    top: 818px;
    font-weight: 800;
    font-size: 34px;
    line-height: 1.2;
    letter-spacing: 0.01em;
    text-transform: uppercase;
  }
  .category-list {
    top: 884px;
    font-weight: 700;
    font-size: 27px;
    line-height: 1.45;
  }
  .store-band {
    height: 132px;
    background: var(--paper);
    display: flex;
    align-items: center;
    justify-content: center;
    padding: 0 24px;
  }
  .store-name {
    color: var(--brand-blue);
    font-weight: 700;
    font-size: 50px;
    letter-spacing: 0.02em;
    text-transform: uppercase;
    white-space: nowrap;
  }
</style>
</head>
<body>
  <main class="poster">
    <section class="sale-panel">
      <svg class="long-shadows" viewBox="0 0 795 1012" aria-hidden="true">
        <polygon points="60,90 300,90 1040,830 800,830" fill="var(--shadow-blue)"/>
        <polygon points="300,90 520,90 1260,830 1040,830" fill="var(--light-blue)" opacity="0.55"/>
        <polygon points="520,90 760,90 1500,830 1260,830" fill="var(--shadow-blue)"/>
        <polygon points="110,440 330,440 740,850 520,850" fill="var(--shadow-blue)"/>
        <polygon points="330,440 700,440 1110,850 740,850" fill="var(--light-blue)" opacity="0.45"/>
      </svg>
      <h1 class="headline-percent">50%</h1>
      <p class="headline-off">Off</p>
      <p class="sticker-note">Every Blue Price Sticker</p>
      <p class="category-list">
        Clothes • Housewares • Kitchenware • Furniture<br>
        Bath and Body • Electronics • Jewelry
      </p>
    </section>
    <footer class="store-band">
      <span class="store-name">Marla's Double Delight</span>
    </footer>
  </main>
</body>
</html>
```